A start-up named "Corvath Therapeutics" - needs a new PowerPoint design

We need a new PowerPoint Design for an early-stage start-up named "Corvath Therapeutics" seeking to disrupt the current approach towards drug discovery within aging disorders.

We would like to build on Corvath's legacy, the founder of the modern science of genetics, by employing a multidisciplinary approach, experimenting, and providing elderly patients the attention they deserve.

We have selected the suffix "therapeutics" intentionally as it stands for (a medicine) the treatment of disease; the science of healing. Alzheimer’s treatment is a huge, urgent, unmet need:
- Shift from a disease-management system to a preventive medicine system
- Focus on increasing the health span, not only the life span

Target Market(s)

Pharma/ Biotech Executives Medical Institutions Healthcare professionals (MDs, nurses, payors, pharmacists, etc.) Patients

Industry/Entity Type

Healthcare

Other font styles liked:
• Celias

Colors
0054AA
0677BA
7BADD7
CADEEF
E8F1F8
E54698
E96AAD
F1A4CE
F9D9EA
FCEFF6
A7469A
B969AE
D3A5CF
EDDBEB
F8F0F9
6B429C
8869AF
B7A5CE
E3DAEB
F3F0F8

Requirements
Must have
• - differentiate from other companies named after Corvath - differentiate from other Pharma/ Biotech companies
Nice to have
• simplicity/ minimalist logo vivid colors gradient 3D Life-Sciences inspired Simple geometry Balance
Should not have
• mascot/ emblem watermark logo animated ink style nature-inspired inventive typography artistic chaos

```html
<!DOCTYPE html>
<html lang="en">
<head>
<meta charset="utf-8">
<title>Corvath Therapeutics – Slide Deck Overview</title>
<link href="https://fonts.googleapis.com/css2?family=Outfit:wght@400;500;600;700&display=swap" rel="stylesheet">
<style>
:root{
  --board:#3d3d3d;
  --num:#d9d9d9;
  --ink:#1f1f2b;
  --muted:#a3a3ad;
  --blue:#2aa9e0;
  --purple:#8c2f9f;
  --violet:#6b429c;
  --pink:#f1a4ce;
  --pink-soft:#f9d9ea;
  --line:#7d6fd2;
  --white:#ffffff;
  --grad:linear-gradient(90deg,#2db3e4 0%,#6a7fd0 50%,#9a3aa6 100%);
}
*{box-sizing:border-box;margin:0;padding:0}
html,body{width:1200px;height:762px;overflow:hidden;background:var(--board)}
body{font-family:"Outfit",sans-serif;color:var(--ink)}
.deck{position:absolute;left:9px;top:5px;display:grid;grid-template-columns:repeat(6,177px);grid-auto-rows:99px;column-gap:24.5px;row-gap:28.5px}
.cell{position:relative}
.slide{position:absolute;inset:0;background:var(--white);overflow:hidden;border-radius:1px}
.num{position:absolute;left:0;top:107px;font-size:8px;color:var(--num);font-weight:500}
.grad{background:var(--grad)}
.a{position:absolute}
.title{position:absolute;font-weight:600;color:var(--ink);line-height:1.05}
.center{left:0;right:0;text-align:center}
.rule{display:block;width:9px;height:1px;background:var(--blue);margin-top:2px}
.center .rule{margin:2px auto 0}
.note{position:absolute;font-size:2.4px;line-height:1.35;color:var(--muted)}
.cap{position:absolute;font-size:2.4px;font-weight:700;letter-spacing:.15px;color:var(--ink);text-transform:uppercase}
.wht{color:var(--white)}
.photo{position:absolute}
.ph-sky{background:linear-gradient(180deg,#5d95b6 0%,#a8b9bf 55%,#3b3a38 100%)}
.ph-lab{background:linear-gradient(135deg,#cfd8df 0%,#7f8c96 50%,#2f3840 100%)}
.ph-wood{background:linear-gradient(135deg,#a3572c 0%,#6d3a21 50%,#2c2220 100%)}
.ph-room{background:linear-gradient(135deg,#e8e6e2 0%,#a7a29c 55%,#55514e 100%)}
.ph-soft{background:linear-gradient(135deg,#d9cfcb 0%,#b4a8a6 50%,#6c6567 100%)}
.ph-dark{background:linear-gradient(135deg,#3c3f4a 0%,#1c1d24 100%)}
.ph-teal{background:linear-gradient(135deg,#bfe3ea 0%,#8fb9c6 55%,#5f8ea2 100%)}
.ph-mist{background:linear-gradient(90deg,#7ec5de 0%,#9d8fbf 55%,#a04ea9 100%)}
.ph-street{background:linear-gradient(90deg,#6c8da6 0%,#9294b7 50%,#a14aa9 100%)}
.ph-map{background:linear-gradient(90deg,#f6c6e1 0%,#cfcfd4 40%,#9b3aa5 65%,#d0d0d6 100%)}
.hex{clip-path:polygon(50% 0,100% 25%,100% 75%,50% 100%,0 75%,0 25%)}
.diamond{position:absolute;border:.7px solid var(--line);border-radius:30%;transform:rotate(45deg);background:var(--white)}
.dtext{position:absolute;text-align:center;font-size:2.3px;line-height:1.3;color:var(--muted)}
.dtext b{display:block;color:var(--ink);font-weight:700;letter-spacing:.1px}
.ring{position:absolute;font-size:5px;font-weight:500;text-align:center}
svg{position:absolute;overflow:visible}
.brand{position:absolute;text-align:center;font-weight:500;line-height:1}
.brand small{display:block;font-weight:500;letter-spacing:.6px}
</style>
</head>
<body>
<main class="deck">

<!-- 1 cover -->
<div class="cell"><section class="slide grad">
  <div class="brand wht center" style="top:38px;font-size:12px">Corvath<small style="font-size:4.2px;margin-top:1px">Therapeutics</small></div>
</section><span class="num">1</span></div>

<!-- 2 quote -->
<div class="cell"><section class="slide">
  <div class="photo ph-room" role="img" aria-label="Businessman seated by an office window" style="left:22px;top:-4px;width:135px;height:74px;border-radius:0 0 70% 55% / 0 0 100% 80%;border:.8px solid #a45cc0"></div>
  <div class="a" style="left:92px;top:71px;width:66px;text-align:center;font-size:4.3px;font-weight:600;line-height:1.25">“Here you can write an inspirational quote”</div>
</section><span class="num">2</span></div>

<!-- 3 history -->
<div class="cell"><section class="slide">
  <div class="a" style="left:31.5px;top:0;width:.7px;height:99px;background:var(--line)"></div>
  <svg width="10" height="10" style="left:27px;top:44px"><circle cx="5" cy="5" r="4.2" fill="#fff" stroke="#7d6fd2" stroke-width=".7"/><text x="5" y="5.9" font-size="2.2" text-anchor="middle" fill="#555">2021</text></svg>
  <div class="title" style="left:41px;top:42px;font-size:4.3px">Company history<br>In timeline<span class="rule"></span></div>
  <div class="note" style="left:41px;top:58px;width:40px">Add a short story about this year and milestone.</div>
  <div class="photo ph-sky" role="img" aria-label="Woman doing yoga on rocks by the sea at dusk" style="left:88px;top:0;width:89px;height:99px"></div>
</section><span class="num">3</span></div>

<!-- 4 history two -->
<div class="cell"><section class="slide">
  <div class="a" style="left:31.5px;top:0;width:.7px;height:99px;background:var(--line)"></div>
  <svg width="10" height="10" style="left:27px;top:25px"><circle cx="5" cy="5" r="4.2" fill="#fff" stroke="#7d6fd2" stroke-width=".7"/><text x="5" y="5.9" font-size="2.2" text-anchor="middle" fill="#555">2019</text></svg>
  <svg width="10" height="10" style="left:27px;top:61px"><circle cx="5" cy="5" r="4.2" fill="#fff" stroke="#7d6fd2" stroke-width=".7"/><text x="5" y="5.9" font-size="2.2" text-anchor="middle" fill="#555">2021</text></svg>
  <div class="title" style="left:40px;top:21px;font-size:4.3px">Company history<br>In timeline<span class="rule"></span></div>
  <div class="note" style="left:40px;top:35px;width:42px">Add a short story about this year and milestone.</div>
  <div class="title" style="left:40px;top:57px;font-size:4.3px">Company history<br>In timeline<span class="rule"></span></div>
  <div class="note" style="left:40px;top:71px;width:42px">Add a short story about this year and milestone.</div>
  <div class="photo ph-lab" role="img" aria-label="Laboratory microscope close-up" style="left:88px;top:0;width:89px;height:99px"></div>
</section><span class="num">4</span></div>

<!-- 5 history -->
<div class="cell"><section class="slide">
  <div class="a" style="left:31.5px;top:0;width:.7px;height:99px;background:var(--line)"></div>
  <svg width="10" height="10" style="left:27px;top:45px"><circle cx="5" cy="5" r="4.2" fill="#fff" stroke="#7d6fd2" stroke-width=".7"/><text x="5" y="5.9" font-size="2.2" text-anchor="middle" fill="#555">2016</text></svg>
  <div class="title" style="left:41px;top:44px;font-size:4.3px">Company history<br>In timeline<span class="rule"></span></div>
  <div class="note" style="left:41px;top:60px;width:40px">Add a short story about this year and milestone.</div>
  <div class="photo ph-wood" role="img" aria-label="Two people seated in chairs on a wooden floor" style="left:88px;top:0;width:89px;height:99px"></div>
</section><span class="num">5</span></div>

<!-- 6 problem -->
<div class="cell"><section class="slide">
  <div class="title" style="left:26px;top:33px;font-size:7.5px">The<br>Problem<span class="rule"></span></div>
  <div class="note" style="left:26px;top:56px;width:34px">Describe the main problem your patients face today.</div>
  <svg width="177" height="99" style="left:0;top:0"><path d="M175 0 C140 18 128 38 135 55 C142 75 160 88 177 99" fill="none" stroke="#8a5dc8" stroke-width=".7"/>
    <g fill="#fff" stroke="#7d6fd2" stroke-width=".6"><circle cx="142" cy="27" r="5"/><circle cx="136" cy="50" r="5"/><circle cx="142" cy="73" r="5"/></g>
    <g fill="none" stroke="#6b429c" stroke-width=".5"><rect x="140.3" y="26" width="3.4" height="2.8"/><path d="M141 26v-1a1 1 0 0 1 2 0v1"/><path d="M134.2 51.8l3.6-3.6"/><path d="M140 71.5h4l-1.5 2v1.5h-1v-1.5z"/></g></svg>
  <div class="cap" style="left:100px;top:21px;width:30px;text-align:right">Problem 1</div>
  <div class="note" style="left:100px;top:24.5px;width:30px;text-align:right">Short note about this problem.</div>
  <div class="cap" style="left:94px;top:44px;width:30px;text-align:right">Problem 2</div>
  <div class="note" style="left:94px;top:47.5px;width:30px;text-align:right">Short note about this problem.</div>
  <div class="cap" style="left:100px;top:67px;width:30px;text-align:right">Problem 3</div>
  <div class="note" style="left:100px;top:70.5px;width:30px;text-align:right">Short note about this problem.</div>
</section><span class="num">6</span></div>

<!-- 7 services -->
<div class="cell"><section class="slide">
  <div class="title" style="left:26px;top:43px;font-size:7.8px">Power best<br>Services<span class="rule"></span></div>
  <svg width="177" height="99" style="left:0;top:0"><g fill="#fff" stroke="#7d6fd2" stroke-width=".6">
    <polygon points="95,22 101,25.5 101,32.5 95,36 89,32.5 89,25.5"/>
    <polygon points="95,42 101,45.5 101,52.5 95,56 89,52.5 89,45.5"/>
    <polygon points="95,62 101,65.5 101,72.5 95,76 89,72.5 89,65.5"/></g>
    <g font-size="2.3" fill="#6b429c" text-anchor="middle"><text x="95" y="29.8">01</text><text x="95" y="49.8">02</text><text x="95" y="69.8">03</text></g></svg>
  <div class="cap" style="left:105px;top:24px">Design</div>
  <div class="note" style="left:105px;top:27px;width:30px">Short service note here.</div>
  <div class="cap" style="left:105px;top:44px">Digital Marketing</div>
  <div class="note" style="left:105px;top:47px;width:30px">Short service note here.</div>
  <div class="cap" style="left:105px;top:64px">Supporting</div>
  <div class="note" style="left:105px;top:67px;width:30px">Short service note here.</div>
</section><span class="num">7</span></div>

<!-- 8 vision -->
<div class="cell"><section class="slide">
  <div class="title" style="left:26px;top:34px;font-size:7.5px">Our<br>Vision<span class="rule"></span></div>
  <div class="note" style="left:26px;top:55px;width:36px">Describe the long term vision of the company.</div>
  <div class="diamond" style="left:101px;top:15px;width:22px;height:22px"></div>
  <div class="diamond" style="left:75px;top:38px;width:22px;height:22px"></div>
  <div class="diamond" style="left:127px;top:38px;width:22px;height:22px"></div>
  <div class="diamond" style="left:101px;top:61px;width:22px;height:22px"></div>
  <div class="dtext" style="left:100px;top:22px;width:24px"><b>Bullet Point</b>Sample text here</div>
  <div class="dtext" style="left:74px;top:45px;width:24px"><b>Bullet Point</b>Sample text here</div>
  <div class="dtext" style="left:126px;top:45px;width:24px"><b>Bullet Point</b>Sample text here</div>
  <div class="dtext" style="left:100px;top:68px;width:24px"><b>Bullet Point</b>Sample text here</div>
</section><span class="num">8</span></div>

<!-- 9 quote photo -->
<div class="cell"><section class="slide">
  <div class="photo ph-mist" role="img" aria-label="Mother and daughter looking out of a window" style="inset:0"></div>
  <div class="a wht" style="left:14px;top:53px;width:72px;text-align:center;font-size:4.3px;font-weight:600;line-height:1.25">“Here you can write another inspirational quote or company goal”</div>
</section><span class="num">9</span></div>

<!-- 10 mission -->
<div class="cell"><section class="slide">
  <div class="photo ph-soft" role="img" aria-label="Elderly couple holding hands on a sofa" style="left:0;top:0;width:49px;height:99px"></div>
  <div class="title" style="left:55px;top:29px;font-size:7.5px">Our<br>Mission<span class="rule"></span></div>
  <div class="note" style="left:55px;top:52px;width:34px">Describe the mission and who we serve.</div>
  <div class="cap" style="left:110px;top:22px">Mission 1</div><div class="note" style="left:110px;top:25px;width:30px">Short mission note here.</div>
  <div class="cap" style="left:110px;top:38px">Mission 2</div><div class="note" style="left:110px;top:41px;width:30px">Short mission note here.</div>
  <div class="cap" style="left:110px;top:54px">Mission 3</div><div class="note" style="left:110px;top:57px;width:30px">Short mission note here.</div>
  <div class="cap" style="left:110px;top:70px">Mission 4</div><div class="note" style="left:110px;top:73px;width:30px">Short mission note here.</div>
</section><span class="num">10</span></div>

<!-- 11 value -->
<div class="cell"><section class="slide">
  <div class="photo ph-room" role="img" aria-label="Patient resting in bed at home" style="left:0;top:10px;width:66px;height:70px;border-radius:40% 60% 55% 45% / 50% 45% 55% 50%;border:.8px solid #7d6fd2"></div>
  <div class="title" style="left:72px;top:24px;font-size:7.5px">Value Proposition</div>
  <div class="note" style="left:72px;top:36px;width:70px">Explain the value we bring to patients, doctors and partners in a few lines.</div>
  <div class="note" style="left:72px;top:50px;width:70px">Explain the value we bring to patients, doctors and partners in a few lines.</div>
</section><span class="num">11</span></div>

<!-- 12 team -->
<div class="cell"><section class="slide">
  <div class="title center" style="top:16px;font-size:7.5px">Meet our team</div>
  <div class="photo ph-soft" role="img" aria-label="Portrait of team member one" style="left:38px;top:33px;width:24px;height:24px;border-radius:50%;border:.8px solid #7d6fd2"></div>
  <div class="photo ph-room" role="img" aria-label="Portrait of team member two" style="left:76px;top:33px;width:24px;height:24px;border-radius:50%;border:.8px solid #7d6fd2"></div>
  <div class="photo ph-teal" role="img" aria-label="Portrait of team member three" style="left:115px;top:33px;width:24px;height:24px;border-radius:50%;border:.8px solid #7d6fd2"></div>
  <div class="dtext" style="left:35px;top:60px;width:30px"><b>Name 1</b>Job position<br>Short bio about this team member.</div>
  <div class="dtext" style="left:73px;top:60px;width:30px"><b>Name 2</b>Job position<br>Short bio about this team member.</div>
  <div class="dtext" style="left:112px;top:60px;width:30px"><b>Name 3</b>Job position<br>Short bio about this team member.</div>
</section><span class="num">12</span></div>

<!-- 13 male vs female -->
<div class="cell"><section class="slide">
  <div class="title center" style="top:9px;font-size:7.2px">Male Vs. Female</div>
  <div class="note center" style="top:18px">Your subtitle in this line</div>
  <svg width="177" height="99" style="left:0;top:0">
    <g fill="none" stroke="#222" stroke-width=".6"><path d="M67 60 C60 40 55 32 44 32"/><path d="M67 60 H44"/><path d="M67 60 C60 75 55 75 44 75"/><path d="M109 60 C116 40 121 32 133 32"/><path d="M109 60 H133"/><path d="M109 60 C116 75 121 75 133 75"/></g>
    <circle cx="77" cy="60" r="11" fill="#2aa9e0"/><circle cx="99" cy="60" r="11" fill="#8c2f9f"/>
    <g fill="#fff"><circle cx="77" cy="55.5" r="1.6"/><rect x="75.2" y="57.6" width="3.6" height="6.5" rx=".8"/><circle cx="99" cy="55.5" r="1.6"/><path d="M97 63.5 L99 57.5 L101 63.5z"/></g>
    <g fill="#fff" stroke="#333" stroke-width=".5"><circle cx="44" cy="32" r="3"/><circle cx="44" cy="53" r="3"/><circle cx="44" cy="75" r="3"/><circle cx="133" cy="32" r="3"/><circle cx="133" cy="53" r="3"/><circle cx="133" cy="75" r="3"/></g></svg>
  <div class="note" style="left:36px;top:36px;width:16px;text-align:center">Short note here</div>
  <div class="note" style="left:36px;top:57px;width:16px;text-align:center">Short note here</div>
  <div class="note" style="left:36px;top:79px;width:16px;text-align:center">Short note here</div>
  <div class="note" style="left:125px;top:36px;width:16px;text-align:center">Short note here</div>
  <div class="note" style="left:125px;top:57px;width:16px;text-align:center">Short note here</div>
  <div class="note" style="left:125px;top:79px;width:16px;text-align:center">Short note here</div>
</section><span class="num">13</span></div>

<!-- 14 gender split -->
<div class="cell"><section class="slide">
  <svg width="177" height="99" style="left:0;top:0">
    <g fill="none" stroke="#8c2f9f" stroke-width="4"><circle cx="67" cy="22" r="9"/><path d="M67 31 V52 M60 42 H74"/></g>
    <g fill="none" stroke="#2aa9e0" stroke-width="4"><circle cx="109" cy="71" r="10"/><path d="M116 64 L127 53"/></g><path d="M121 50 H131 V60z" fill="#2aa9e0"/>
    <g fill="none" stroke="#2aa9e0" stroke-width=".5"><circle cx="25" cy="44" r="1.2"/><path d="M23.6 46h2.8v4h-2.8z"/><circle cx="31" cy="44" r="1.2"/><path d="M29.6 46h2.8v4h-2.8z"/><circle cx="25" cy="57" r="1.2"/><path d="M23.6 59h2.8v4h-2.8z"/><circle cx="31" cy="57" r="1.2"/><path d="M29.6 59h2.8v4h-2.8z"/><circle cx="25" cy="70" r="1.2"/><path d="M23.6 72h2.8v4h-2.8z"/><circle cx="31" cy="70" r="1.2"/><path d="M29.6 72h2.8v4h-2.8z"/><circle cx="144" cy="25" r="1.2"/><path d="M142.6 27h2.8v4h-2.8z"/><circle cx="150" cy="25" r="1.2"/><path d="M148.6 27h2.8v4h-2.8z"/><circle cx="144" cy="43" r="1.2"/><path d="M142.6 45h2.8v4h-2.8z"/><circle cx="150" cy="43" r="1.2"/><path d="M148.6 45h2.8v4h-2.8z"/></g></svg>
  <div class="a" style="left:54px;top:56px;width:26px;text-align:center;font-size:5px;font-weight:700;line-height:1">60%<br><span style="font-size:3.4px">WOMEN</span></div>
  <div class="note" style="left:52px;top:66px;width:30px;text-align:center">Short note about women.</div>
  <div class="a" style="left:98px;top:17px;width:26px;text-align:center;font-size:5px;font-weight:700;line-height:1">40%<br><span style="font-size:3.4px">MEN</span></div>
  <div class="note" style="left:96px;top:27px;width:30px;text-align:center">Short note about men.</div>
</section><span class="num">14</span></div>

<!-- 15 data charts -->
<div class="cell"><section class="slide">
  <div class="title center" style="top:9px;font-size:7.2px">Data Charts</div>
  <div class="note center" style="top:18px">Your subtitle in this line</div>
  <svg width="177" height="99" style="left:0;top:0">
    <circle cx="88" cy="58" r="13" fill="none" stroke="#f1a4ce" stroke-width="4"/>
    <path d="M88 45 A13 13 0 0 1 101 58" fill="none" stroke="#2aa9e0" stroke-width="4"/>
    <path d="M101 58 A13 13 0 0 1 88 71" fill="none" stroke="#cadeef" stroke-width="4"/>
    <g fill="#fff" stroke="#bbb" stroke-width=".4"><circle cx="70" cy="32" r="2.6"/><circle cx="67" cy="57" r="2.6"/><circle cx="70" cy="80" r="2.6"/><circle cx="106" cy="32" r="2.6"/><circle cx="110" cy="57" r="2.6"/><circle cx="106" cy="80" r="2.6"/></g></svg>
  <div class="note" style="left:37px;top:30px;width:28px;text-align:right"><b style="color:#222">Title goes here</b><br>Short note here</div>
  <div class="note" style="left:33px;top:55px;width:28px;text-align:right"><b style="color:#222">Title goes here</b><br>Short note here</div>
  <div class="note" style="left:37px;top:78px;width:28px;text-align:right"><b style="color:#222">Title goes here</b><br>Short note here</div>
  <div class="note" style="left:112px;top:30px;width:28px"><b style="color:#222">Title goes here</b><br>Short note here</div>
  <div class="note" style="left:116px;top:55px;width:28px"><b style="color:#222">Title goes here</b><br>Short note here</div>
  <div class="note" style="left:112px;top:78px;width:28px"><b style="color:#222">Title goes here</b><br>Short note here</div>
</section><span class="num">15</span></div>

<!-- 16 complementary -->
<div class="cell"><section class="slide">
  <div class="photo ph-dark hex" role="img" aria-label="Hands clasped in dark lighting" style="left:25px;top:20px;width:60px;height:64px"></div>
  <div class="title" style="left:92px;top:31px;font-size:7px">Complementary<br>Information<span class="rule"></span></div>
  <div class="note" style="left:92px;top:52px;width:56px">Add supporting details that help the audience understand the topic.</div>
</section><span class="num">16</span></div>

<!-- 17 extra -->
<div class="cell"><section class="slide grad">
  <div class="title wht" style="left:25px;top:24px;font-size:8px">Extra</div>
  <div class="photo ph-room" role="img" aria-label="Man reading by a bright window" style="left:73px;top:9px;width:31px;height:45px"></div>
  <div class="photo ph-room" role="img" aria-label="Woman working at a desk" style="left:26px;top:45px;width:31px;height:44px"></div>
  <div class="photo ph-teal" role="img" aria-label="Person walking along a beach" style="left:120px;top:45px;width:31px;height:44px"></div>
  <div class="note wht" style="left:73px;top:62px;width:38px;font-weight:600">Short note about this extra content here.</div>
</section><span class="num">17</span></div>

<!-- 18 roadmap -->
<div class="cell"><section class="slide">
  <div class="a" style="left:30px;top:33px;width:115px;height:.7px;background:var(--line)"></div>
  <div class="diamond" style="left:29px;top:24px;width:18px;height:18px"></div>
  <div class="diamond" style="left:64px;top:24px;width:18px;height:18px"></div>
  <div class="diamond" style="left:99px;top:24px;width:18px;height:18px"></div>
  <div class="diamond" style="left:134px;top:24px;width:18px;height:18px"></div>
  <div class="dtext" style="left:28px;top:30px;width:20px"><b>2019</b>Title and text</div>
  <div class="dtext" style="left:63px;top:30px;width:20px"><b>2023</b>Title and text</div>
  <div class="dtext" style="left:98px;top:30px;width:20px"><b>2026</b>Title and text</div>
  <div class="dtext" style="left:133px;top:30px;width:20px"><b>2030</b>Title and text</div>
  <div class="title" style="left:36px;top:59px;font-size:6.8px;text-align:right">Company<br>Roadmap<span class="rule" style="margin-left:auto"></span></div>
  <div class="note" style="left:75px;top:59px;width:72px">Describe the key steps planned for the next years of growth.</div>
</section><span class="num">18</span></div>

<!-- 19 financials -->
<div class="cell"><section class="slide">
  <svg width="177" height="99" style="left:0;top:0">
    <g stroke="#e3e3e3" stroke-width=".3"><path d="M33 10H96M33 20H96M33 30H96M33 40H96M33 50H96M33 60H96M33 70H96"/></g>
    <path d="M33 8V74H96" fill="none" stroke="#666" stroke-width=".4"/>
    <polyline points="35,72 41,64 47,58 53,52 59,44 65,38 71,33 77,30 83,29 89,28 95,32" fill="none" stroke="#8c2f9f" stroke-width=".8"/>
    <polyline points="35,73 41,70 47,68 53,66 59,60 65,62 71,55 77,46 83,42 89,38 95,45" fill="none" stroke="#2aa9e0" stroke-width=".8"/></svg>
  <div class="title" style="left:109px;top:26px;font-size:7.2px">Financials<span class="rule"></span></div>
  <div class="note" style="left:109px;top:38px;width:40px">Describe the financial results and outlook.</div>
</section><span class="num">19</span></div>

<!-- 20 butterfly bars -->
<div class="cell"><section class="slide">
  <svg width="177" height="99" style="left:0;top:0">
    <path d="M12 12V75M164 12V75M12 75H164" fill="none" stroke="#ddd" stroke-width=".4"/>
    <g fill="#8c2f9f"><rect x="82" y="29" width="7" height="4"/><rect x="77" y="34" width="12" height="4"/><rect x="72" y="39" width="17" height="4"/><rect x="60" y="44" width="29" height="4"/><rect x="22" y="49" width="67" height="4"/><rect x="32" y="54" width="57" height="4"/><rect x="30" y="59" width="59" height="4"/><rect x="36" y="64" width="53" height="4"/></g>
    <g fill="#2aa9e0"><rect x="89" y="29" width="4" height="4"/><rect x="89" y="34" width="6" height="4"/><rect x="89" y="39" width="10" height="4"/><rect x="89" y="44" width="24" height="4"/><rect x="89" y="49" width="69" height="4"/><rect x="89" y="54" width="55" height="4"/><rect x="89" y="59" width="61" height="4"/><rect x="89" y="64" width="52" height="4"/></g></svg>
  <div class="note" style="left:12px;top:81px;width:52px"><b style="color:#8c2f9f">YOUR TITLE HERE</b><br>Short note about this data.</div>
  <div class="note" style="left:104px;top:81px;width:52px"><b style="color:#2aa9e0">YOUR TITLE HERE</b><br>Short note about this data.</div>
</section><span class="num">20</span></div>

<!-- 21 pie -->
<div class="cell"><section class="slide">
  <div class="title center" style="top:13px;font-size:7.2px">Pie normal chart<span class="rule"></span></div>
  <svg width="177" height="99" style="left:0;top:0"><g fill="none" stroke-width=".8">
    <circle cx="39" cy="49" r="12" stroke="#e6e6ee"/><path d="M39 37 A12 12 0 0 1 50.4 45.3" stroke="#6b7fd2"/>
    <circle cx="72" cy="49" r="12" stroke="#e6e6ee"/><path d="M72 37 A12 12 0 1 1 60 49" stroke="#6b7fd2"/>
    <circle cx="105" cy="49" r="12" stroke="#e6e6ee"/><path d="M105 37 A12 12 0 0 1 105 61" stroke="#6b7fd2"/>
    <circle cx="138" cy="49" r="12" stroke="#e6e6ee"/><path d="M138 37 A12 12 0 1 1 126 49" stroke="#6b7fd2"/></g></svg>
  <div class="ring" style="left:27px;top:46px;width:24px">15%</div>
  <div class="ring" style="left:60px;top:46px;width:24px">75%</div>
  <div class="ring" style="left:93px;top:46px;width:24px">50%</div>
  <div class="ring" style="left:126px;top:46px;width:24px">75%</div>
  <div class="dtext" style="left:25px;top:66px;width:28px"><b>Your Title</b>Short note here</div>
  <div class="dtext" style="left:58px;top:66px;width:28px"><b>Your Title</b>Short note here</div>
  <div class="dtext" style="left:91px;top:66px;width:28px"><b>Your Title</b>Short note here</div>
  <div class="dtext" style="left:124px;top:66px;width:28px"><b>Your Title</b>Short note here</div>
</section><span class="num">21</span></div>

<!-- 22 doctors -->
<div class="cell"><section class="slide">
  <div class="photo ph-lab" role="img" aria-label="Portrait of a doctor wearing a mask" style="left:45px;top:25px;width:23px;height:23px;border-radius:50%;border:.8px solid #7d6fd2"></div>
  <div class="photo ph-soft" role="img" aria-label="Portrait of a smiling doctor" style="left:107px;top:25px;width:23px;height:23px;border-radius:50%;border:.8px solid #7d6fd2"></div>
  <div class="a" style="left:88px;top:24px;width:.5px;height:62px;background:#ddd"></div>
  <div class="dtext" style="left:36px;top:53px;width:42px"><b>Doctor 1</b>Specialist<br><br>Short note about this doctor.</div>
  <div class="dtext" style="left:98px;top:53px;width:42px"><b>Doctor 2</b>Specialist<br><br>Short note about this doctor.</div>
</section><span class="num">22</span></div>

<!-- 23 quote street -->
<div class="cell"><section class="slide">
  <div class="photo ph-street" role="img" aria-label="Elderly man walking along a waterfront promenade" style="inset:0"></div>
  <div class="a wht" style="left:96px;top:32px;width:66px;text-align:center;font-size:4.2px;font-weight:600;line-height:1.25">“Here you can write another inspirational quote or company goal”</div>
</section><span class="num">23</span></div>

<!-- 24 diamond cycle -->
<div class="cell"><section class="slide">
  <div class="diamond" style="left:63px;top:25px;width:50px;height:50px;border-color:#8a5dc8"></div>
  <svg width="177" height="99" style="left:0;top:0"><g fill="#fff" stroke="#7d6fd2" stroke-width=".6"><circle cx="88" cy="25" r="5"/><circle cx="63" cy="50" r="5"/><circle cx="114" cy="50" r="5"/><circle cx="88" cy="74" r="5"/></g></svg>
  <div class="note" style="left:106px;top:12px;width:30px"><b style="color:#222">BRANDING DESIGN</b><br>Short note here</div>
  <div class="note" style="left:26px;top:43px;width:30px;text-align:right"><b style="color:#222">UI UX DESIGN</b><br>Short note here</div>
  <div class="note" style="left:126px;top:43px;width:30px"><b style="color:#222">SOCIAL MEDIA</b><br>Short note here</div>
  <div class="note" style="left:100px;top:80px;width:30px"><b style="color:#222">WEB DESIGN</b><br>Short note here</div>
</section><span class="num">24</span></div>

<!-- 25 strip features -->
<div class="cell"><section class="slide">
  <div class="photo ph-teal" role="img" aria-label="Laboratory vials in blue light" style="left:68px;top:0;width:41px;height:99px"></div>
  <div class="dtext" style="left:30px;top:24px;width:32px"><b style="color:#2aa9e0">●</b><b>Your Title Here</b>Short note about this item.</div>
  <div class="dtext" style="left:115px;top:24px;width:32px"><b style="color:#2aa9e0">●</b><b>Your Title Here</b>Short note about this item.</div>
  <div class="dtext" style="left:30px;top:58px;width:32px"><b style="color:#2aa9e0">●</b><b>Your Title Here</b>Short note about this item.</div>
  <div class="dtext" style="left:115px;top:58px;width:32px"><b style="color:#2aa9e0">●</b><b>Your Title Here</b>Short note about this item.</div>
</section><span class="num">25</span></div>

<!-- 26 timeline infographic -->
<div class="cell"><section class="slide">
  <div class="title center" style="top:10px;font-size:7px">Timeline Infographic</div>
  <div class="note center" style="top:19px">Enter your subhead line here</div>
  <svg width="177" height="99" style="left:0;top:0">
    <path d="M47 65 C47 52 64 47 64 47 M80 47 C80 60 97 65 97 65 M80 47 C80 36 97 36 97 47 M113 47 C113 60 130 65 130 65" fill="none" stroke="#cadeef" stroke-width=".6"/>
    <circle cx="72" cy="47" r="7.5" fill="#7badd7" stroke="#cadeef" stroke-width="1.5"/><circle cx="105" cy="47" r="7.5" fill="#7badd7" stroke="#cadeef" stroke-width="1.5"/>
    <circle cx="55" cy="65" r="7.5" fill="#f9d9ea" stroke="#fcefF6" stroke-width="1.5"/><circle cx="89" cy="65" r="7.5" fill="#f9d9ea" stroke="#fcefF6" stroke-width="1.5"/><circle cx="122" cy="65" r="7.5" fill="#f9d9ea" stroke="#fcefF6" stroke-width="1.5"/>
    <g font-size="2.4" text-anchor="middle" fill="#fff"><text x="72" y="47.8">2019</text><text x="105" y="47.8">2017</text><text x="55" y="65.8">2014</text><text x="89" y="65.8">2015</text><text x="122" y="65.8">2018</text></g></svg>
  <div class="dtext" style="left:22px;top:38px;width:30px"><b>Your Title Here</b>Short note about this year.</div>
  <div class="dtext" style="left:125px;top:38px;width:30px"><b>Your Title Here</b>Short note about this year.</div>
  <div class="dtext" style="left:22px;top:75px;width:30px"><b>Your Title Here</b>Short note about this year.</div>
  <div class="dtext" style="left:74px;top:75px;width:30px"><b>Your Title Here</b>Short note about this year.</div>
  <div class="dtext" style="left:125px;top:75px;width:30px"><b>Your Title Here</b>Short note about this year.</div>
</section><span class="num">26</span></div>

<!-- 27 photo grid -->
<div class="cell"><section class="slide grad">
  <div class="photo ph-room" role="img" aria-label="Smiling doctor in a clinic" style="left:25px;top:9px;width:63px;height:40px"></div>
  <div class="photo ph-soft" role="img" aria-label="Nurse caring for a patient" style="left:89px;top:9px;width:63px;height:40px"></div>
  <div class="photo ph-lab" role="img" aria-label="Medical team at work" style="left:25px;top:50px;width:63px;height:41px"></div>
  <div class="photo ph-room" role="img" aria-label="Tired man rubbing his eyes" style="left:89px;top:50px;width:63px;height:41px"></div>
  <div class="a" style="left:60px;top:39px;width:57px;height:27px;background:#fff;display:flex;align-items:center;justify-content:center;text-align:center;font-size:4.3px;font-weight:700;letter-spacing:.4px;line-height:1.05">I HATE GETTING<br>UP IN THE<br>MORNING</div>
</section><span class="num">27</span></div>

<!-- 28 world maps -->
<div class="cell"><section class="slide">
  <div class="title center" style="top:15px;font-size:7.2px">World Maps<span class="rule"></span></div>
  <div class="photo ph-map" role="img" aria-label="World map with highlighted regions in pink, purple and blue" style="left:30px;top:31px;width:112px;height:54px;border-radius:18px 22px 14px 20px;opacity:.85"></div>
</section><span class="num">28</span></div>

<!-- 29 competition -->
<div class="cell"><section class="slide">
  <div class="title center" style="top:17px;font-size:7.2px">Our competition<span class="rule"></span></div>
  <div class="diamond" style="left:33px;top:45px;width:24px;height:24px"></div>
  <div class="diamond" style="left:76px;top:45px;width:24px;height:24px"></div>
  <div class="diamond" style="left:121px;top:45px;width:24px;height:24px"></div>
  <div class="dtext" style="left:31px;top:52px;width:28px"><b>Competitor 1</b>Short note here</div>
  <div class="dtext" style="left:74px;top:52px;width:28px"><b>Competitor 2</b>Short note here</div>
  <div class="dtext" style="left:119px;top:52px;width:28px"><b>Competitor 3</b>Short note here</div>
</section><span class="num">29</span></div>

<!-- 30 analysis -->
<div class="cell"><section class="slide">
  <div class="title center" style="top:9px;font-size:7.2px">Analysis</div>
  <div class="note center" style="top:18px">Your subtitle in this line</div>
  <svg width="177" height="99" style="left:0;top:0">
    <circle cx="70" cy="29" r="3" fill="#2aa9e0"/><path d="M65 34h10v12h-2v17h-2.5v-12h-1v12H67V46h-2z" fill="#2aa9e0"/>
    <circle cx="106" cy="29" r="3" fill="#8c2f9f"/><path d="M103 34h6l3.5 14h-3v15h-2.5V52h-1v11h-2.5V48h-3z" fill="#8c2f9f"/>
    <path d="M88 27V78" stroke="#ddd" stroke-width=".5"/></svg>
  <div class="a" style="left:58px;top:65px;width:24px;text-align:center;font-size:3px;font-weight:600">Men<br><span style="font-size:7px;color:#2aa9e0">55%</span></div>
  <div class="a" style="left:94px;top:65px;width:24px;text-align:center;font-size:3px;font-weight:600">Women<br><span style="font-size:7px;color:#8c2f9f">65%</span></div>
  <div class="note" style="left:58px;top:84px;width:24px;text-align:center">Short note here</div>
  <div class="note" style="left:94px;top:84px;width:24px;text-align:center">Short note here</div>
</section><span class="num">30</span></div>

<!-- 31 more info -->
<div class="cell"><section class="slide grad">
  <div class="title wht" style="left:25px;top:47px;font-size:7.5px">More<br>Information</div>
  <div class="photo ph-room" role="img" aria-label="Doctor writing notes at a desk" style="left:78px;top:9px;width:31px;height:33px"></div>
  <div class="photo ph-soft" role="img" aria-label="Two people talking in an office" style="left:120px;top:44px;width:31px;height:45px"></div>
  <div class="note wht" style="left:78px;top:55px;width:32px;font-weight:600">Short note about more information here.</div>
</section><span class="num">31</span></div>

<!-- 32 business model -->
<div class="cell"><section class="slide">
  <div class="title" style="left:26px;top:33px;font-size:7px">Bussiness<br>Model<span class="rule"></span></div>
  <div class="note" style="left:26px;top:52px;width:36px">Describe how the business creates value.</div>
  <svg width="177" height="99" style="left:0;top:0"><polygon points="116,25 137,37 137,61 116,73 95,61 95,37" fill="#fff" stroke="#7d6fd2" stroke-width=".6"/></svg>
  <div class="brand" style="left:101px;top:46px;width:30px;font-size:4.5px;color:var(--blue)">Corvath<small style="font-size:1.8px">Therapeutics</small></div>
  <div class="photo ph-dark hex" role="img" aria-label="City buildings" style="left:109px;top:10px;width:15px;height:16px"></div>
  <div class="photo ph-room hex" role="img" aria-label="Person at work" style="left:89px;top:21px;width:15px;height:16px"></div>
  <div class="photo ph-soft hex" role="img" aria-label="Hands holding a cup" style="left:129px;top:21px;width:15px;height:16px"></div>
  <div class="photo ph-teal hex" role="img" aria-label="Laboratory glassware" style="left:89px;top:61px;width:15px;height:16px"></div>
  <div class="photo ph-street hex" role="img" aria-label="Smartphone with app icons" style="left:129px;top:61px;width:15px;height:16px"></div>
  <div class="photo ph-lab hex" role="img" aria-label="Modern office interior" style="left:109px;top:73px;width:15px;height:16px"></div>
</section><span class="num">32</span></div>

<!-- 33 mobile app -->
<div class="cell"><section class="slide">
  <div class="title center" style="top:16px;font-size:6.5px">Mobile Application<span class="rule"></span></div>
  <div class="note" style="left:28px;top:33px;width:121px;text-align:center;color:#555">Describe the mobile application and how patients and doctors use it every day to stay informed.</div>
  <div class="a" style="left:69px;top:52px;width:40px;height:52px;border:.6px solid #bbb;border-radius:5px"></div>
  <div class="a" style="left:86px;top:55px;width:6px;height:.8px;background:#bbb;border-radius:1px"></div>
  <div class="brand" style="left:74px;top:76px;width:30px;font-size:4.5px;color:var(--blue)">Corvath<small style="font-size:1.8px">Therapeutics</small></div>
</section><span class="num">33</span></div>

<!-- 34 pricing table -->
<div class="cell"><section class="slide">
  <svg width="177" height="99" style="left:0;top:0">
    <g fill="none" stroke="#8cb8e0" stroke-width=".4"><circle cx="88" cy="24" r="2"/><circle cx="113" cy="24" r="2"/><circle cx="139" cy="24" r="2"/></g>
    <g stroke="#e2e2e2" stroke-width=".3"><path d="M25 39H151M25 48H151M25 57H151M25 65H151M25 74H151"/></g>
    <path d="M25 78H151" stroke="#444" stroke-width=".4"/>
    <g fill="none" stroke="#999" stroke-width=".3"><circle cx="88" cy="61" r="1.1"/><circle cx="113" cy="61" r="1.1"/><circle cx="139" cy="61" r="1.1"/><circle cx="113" cy="70" r="1.1"/><circle cx="139" cy="70" r="1.1"/><path d="M87 69l2 2M89 69l-2 2"/></g>
    <g font-size="2.2" fill="#555" text-anchor="middle"><text x="88" y="31">SMALL</text><text x="88" y="33.5">SERVICE</text><text x="113" y="31">SMALL</text><text x="113" y="33.5">SERVICE</text><text x="139" y="31">PREMIUM</text><text x="139" y="33.5">SERVICE</text>
      <text x="88" y="44">20</text><text x="113" y="44">50</text><text x="139" y="44">100</text><text x="88" y="53">3</text><text x="113" y="53">10</text><text x="139" y="53">50</text><text x="88" y="83">$10</text><text x="113" y="83">$25</text><text x="139" y="83">$50</text></g>
    <g font-size="2.2" fill="#555"><text x="26" y="44">Number of</text><text x="26" y="53">Number of</text><text x="26" y="62">Detailed</text><text x="26" y="71">Priority answers</text></g></svg>
</section><span class="num">34</span></div>

<!-- 35 questions -->
<div class="cell"><section class="slide">
  <div class="title" style="left:33px;top:45px;font-size:7px;text-align:right">Questions<span class="rule" style="margin-left:auto"></span></div>
  <div class="photo ph-soft hex" role="img" aria-label="Woman smiling with hand near her face" style="left:70px;top:30px;width:37px;height:41px"></div>
  <div class="note" style="left:111px;top:45px;width:36px">Short note about questions and answers.</div>
</section><span class="num">35</span></div>

<!-- 36 closing -->
<div class="cell"><section class="slide">
  <div class="brand center" style="top:40px;font-size:11px;color:var(--blue)">Corvath<small style="font-size:4px;margin-top:1px">Therapeutics</small></div>
</section><span class="num">36</span></div>

</main>
</body>
</html>
```